Business Card for By Karel Voss

Looking to have a business card designed for my lifestyle and fitness company. My company offers personal training, online programming and nutrition advice based out of London, United Kingdom.

I'd like to see modern, sleek designs, focusing on black, matte black or matte grey. Design doesn't need to be overly descriptive as this will also be used as a personal business card. I've included my logo.

Please note that my company is no longer called "Fitness by Karel Voss" but instead "By Karel Voss", this is because of my other ventures. Therefore please don't use the "fitness by karel voss" text.

information about my company can be found at www.bykarelvoss.com

Company is also based out of London (United Kingdom) & Sydney (Australia) this could be reflected on the card.

Industry/Entity Type

Business

Contact Information for Business Card

Karel Voss
+44 7382 615027
karel@bykarelvoss.com
www.bykarelvoss.com

Font styles to use
Sans Serif

Requirements
Must have
• All contact details and inclusion of my logo.

```html
<!DOCTYPE html>
<html lang="en">
<head>
<meta charset="utf-8">
<title>By Karel Voss — Business Card</title>
<link rel="stylesheet" href="https://fonts.googleapis.com/css2?family=Arimo:wght@400;700&family=Tinos:wght@400;700&display=swap">
<style>
  :root {
    --backdrop: #e6e2dc;
    --card-black: #1f1c1b;
    --card-white: #ffffff;
    --ink: #151312;
    --ink-soft: #4a423c;
    --tagline: #8b8681;
    --light-text: #ffffff;
  }
  * { margin: 0; padding: 0; box-sizing: border-box; }
  html, body {
    width: 1200px; height: 582px; overflow: hidden;
    background: var(--backdrop);
  }
  .canvas {
    position: relative; width: 1200px; height: 582px;
    display: flex; align-items: center; justify-content: center; gap: 40px;
  }
  .card {
    position: relative; width: 560px; height: 318px;
    border-radius: 16px; overflow: hidden;
    box-shadow: 0 6px 14px rgba(0,0,0,0.25);
  }

  /* Front */
  .card--front {
    background: radial-gradient(ellipse at 50% 40%, #2a2625 0%, var(--card-black) 70%);
    color: var(--light-text);
  }
  .brand-lockup {
    position: absolute; left: 0; right: 0;
    display: flex; flex-direction: column; align-items: center; gap: 10px;
  }
  .card--front .brand-lockup { top: 62px; }
  .brand-dot {
    width: 44px; height: 44px; border-radius: 50%;
  }
  .card--front .brand-dot { background: var(--light-text); }
  .brand-name {
    font-family: "Arimo", Arial, sans-serif; font-weight: 700;
    font-size: 26px; letter-spacing: 1px; text-transform: uppercase; white-space: nowrap;
  }
  .tagline {
    position: absolute; left: 0; right: 0; top: 246px; text-align: center;
    font-family: "Arimo", Arial, sans-serif; font-weight: 700; font-size: 12.5px;
    letter-spacing: 0.6px; color: var(--tagline);
  }

  /* Back */
  .card--back { background: var(--card-white); color: var(--ink); }
  .card-shapes { position: absolute; inset: 0; width: 100%; height: 100%; }
  .name-tab {
    position: absolute; left: 0; top: 38px; width: 62px; height: 33px;
    background: var(--card-black);
  }
  .person-name {
    position: absolute; left: 140px; top: 36px;
    font-family: "Tinos", "Times New Roman", serif; font-weight: 700; font-size: 28px;
  }
  .person-role {
    position: absolute; left: 140px; top: 74px;
    font-family: "Tinos", "Times New Roman", serif; font-weight: 700; font-size: 15px;
    letter-spacing: 1.6px; color: var(--ink-soft);
  }
  .contact-list { position: absolute; left: 64px; top: 136px; list-style: none; }
  .contact-item {
    display: flex; align-items: center; gap: 14px; height: 20px; margin-bottom: 42px;
    font-family: "Arimo", Arial, sans-serif; font-weight: 700; font-size: 13px;
  }
  .contact-icon { width: 26px; height: 18px; fill: var(--ink); }
  .card--back .brand-lockup { left: 360px; right: 14px; top: 100px; }
  .card--back .brand-dot { background: var(--ink); }
  .card--back .brand-name { font-size: 22px; color: var(--ink); }
  .website, .location {
    position: absolute;
    font-family: "Arimo", Arial, sans-serif; font-weight: 700; font-size: 12px;
    letter-spacing: 0.6px; color: var(--light-text);
  }
  .website { left: 42px; top: 292px; }
  .location { left: 418px; top: 274px; }
</style>
</head>
<body>
<main class="canvas">
  <section class="card card--front" aria-label="Business card front">
    <div class="brand-lockup">
      <span class="brand-dot"></span>
      <span class="brand-name">By Karel Voss</span>
    </div>
    <p class="tagline">Personal training | Online programming | Nutrition advice</p>
  </section>

  <section class="card card--back" aria-label="Business card back">
    <svg class="card-shapes" viewBox="0 0 560 318" preserveAspectRatio="none" aria-hidden="true">
      <polygon points="0,272 306,272 274,318 0,318" fill="var(--card-black)"/>
      <polygon points="284,318 338,237 560,237 560,318" fill="var(--card-black)"/>
    </svg>
    <div class="name-tab"></div>
    <h1 class="person-name">Karel Voss</h1>
    <p class="person-role">Personal trainer</p>
    <ul class="contact-list">
      <li class="contact-item">
        <svg class="contact-icon" viewBox="0 0 26 18" aria-hidden="true">
          <path d="M1 6 Q13 -2 25 6 L22 9 L18 7 L18 5 Q13 3 8 5 L8 7 L4 9 Z"/>
          <path d="M6 10 L9 7 L17 7 L20 10 L21 17 L5 17 Z"/>
          <circle cx="13" cy="12" r="2.4" fill="#fff"/>
        </svg>
        <span>+44 7382 615027</span>
      </li>
      <li class="contact-item">
        <svg class="contact-icon" viewBox="0 0 26 18" aria-hidden="true">
          <rect x="1" y="2" width="24" height="15"/>
          <path d="M2 3 L13 11 L24 3 M2 16 L10 9 M24 16 L16 9" stroke="#fff" stroke-width="1.3" fill="none"/>
        </svg>
        <span>karel@bykarelvoss.com</span>
      </li>
    </ul>
    <div class="brand-lockup">
      <span class="brand-dot"></span>
      <span class="brand-name">By Karel Voss</span>
    </div>
    <p class="website">www.bykarelvoss.com</p>
    <p class="location">London, United Kingdom</p>
  </section>
</main>
</body>
</html>
```